Label for Refill packaging eco-conscious beauty brand

We need a label for our refill pouch. Velvet Harbor is an unscented conditioner formulated using the finest healthy & pure ingredients, free of chemicals and harmful toxins. As a minimalist beauty brand we are proud to be certified with TPL, VerdaSeal and Silver Fawn.

We already have the pouches and an exciting label for our regular bottles.
We choose a kraft brown packing for the refill pouch and would like something minimalist but elegant for the label.

```html
<!DOCTYPE html>
<html lang="en">
<head>
<meta charset="utf-8">
<title>Velvet Harbor – Refill Pouch Label</title>
<link rel="stylesheet" href="https://fonts.googleapis.com/css2?family=Montserrat:wght@300;400;600&display=swap">
<style>
  :root {
    --backdrop: #8a80ad;
    --kraft: #c8a57b;
    --kraft-light: #d0b089;
    --kraft-dark: #bf9b70;
    --mauve: #876a70;
    --gold-dark: #c8961a;
    --gold-mid: #f4d777;
    --gold-light: #fff1b0;
  }
  * { margin: 0; padding: 0; box-sizing: border-box; }
  html, body {
    width: 1200px;
    height: 899px;
    overflow: hidden;
    background: var(--backdrop);
  }
  .label {
    position: absolute;
    left: 221px;
    top: 40px;
    width: 757px;
    height: 820px;
    background: radial-gradient(ellipse at 40% 30%, var(--kraft-light), var(--kraft) 55%, var(--kraft-dark));
    font-family: "Montserrat", sans-serif;
    color: var(--mauve);
  }
  .label__frame {
    position: absolute;
    inset: 8px;
    border: 2px solid var(--mauve);
    border-radius: 10px;
  }
  .band {
    position: absolute;
    left: 284px;
    width: 191px;
  }
  .band--mauve { background: var(--mauve); }
  .band--gold {
    background: linear-gradient(180deg, var(--gold-dark), var(--gold-mid) 35%, var(--gold-light) 55%, var(--gold-mid) 75%, var(--gold-dark));
  }
  .band--top { top: 10px; height: 247px; }
  .band--top-gold { top: 257px; height: 20px; }
  .band--bottom-gold { top: 721px; height: 21px; }
  .band--bottom { top: 744px; height: 68px; }
  .leaf-illustration {
    position: absolute;
    left: 286px;
    top: 314px;
    width: 185px;
    height: 193px;
  }
  .product-name {
    position: absolute;
    left: 0;
    right: 0;
    top: 540px;
    text-align: center;
    font-weight: 600;
    font-size: 48px;
    line-height: 50px;
  }
  .product-desc {
    position: absolute;
    left: 0;
    right: 0;
    top: 650px;
    text-align: center;
    font-weight: 300;
    font-size: 19px;
    line-height: 24px;
    letter-spacing: 0.2px;
  }
</style>
</head>
<body>
  <main class="label">
    <div class="label__frame"></div>
    <div class="band band--mauve band--top"></div>
    <div class="band band--gold band--top-gold"></div>
    <svg class="leaf-illustration" role="img" aria-label="Line illustration of a leaf with branching veins" viewBox="0 0 185 193">
      <rect width="185" height="193" fill="var(--mauve)" opacity="0.22"/>
    </svg>
    <h1 class="product-name">Velvet<br>Harbor</h1>
    <p class="product-desc">unscented hair conditioner<br>après-shampoing non parfumé</p>
    <div class="band band--gold band--bottom-gold"></div>
    <div class="band band--mauve band--bottom"></div>
  </main>
</body>
</html>
```